Web Design Project - Pinecrest & Tours

Live long and prosper!
The page aims people willing to book holidays and health prevention courses in combination. The ZUR-Method is a concept of defined:
* EXERCISES: walking, fitness, yoga, ...
* RELAXATION: massage, spa, ...
* NUTRITION: diets (more, less, selected)
Doing in a group brings fun and social community.
When wanted a doctor or health professional supports the stay.
The page explains all courses, all benefits and all locations to stay.
Health

```html
<!DOCTYPE html>
<html lang="de">
<head>
<meta charset="utf-8">
<title>Pinecrest &amp; Tours</title>
<link rel="stylesheet" href="https://fonts.googleapis.com/css2?family=Source+Sans+3:wght@400;600&display=swap">
<style>
:root{
  --green:#8cc63f;
  --green-dark:#7fb534;
  --green-light:#a9d65e;
  --green-pale:#e6f2d3;
  --text:#3d3d3d;
  --white:#fff;
  --orange:#e07a3c;
}
*{margin:0;padding:0;box-sizing:border-box}
html,body{width:1050px;height:1200px;overflow:hidden}
body{font-family:"Source Sans 3",sans-serif;color:var(--text);background:var(--white);position:relative}
.header{position:absolute;left:0;top:0;width:1050px;height:518px;background:linear-gradient(#fbfbf4 0,#f1f1ec 116px,#f6f6f4 118px,#eeeeee 518px)}
.brand{position:absolute;left:70px;top:30px;width:130px;text-align:center}
.brand-mark{width:30px;height:30px;border-radius:50%;background:var(--orange);margin:0 auto 8px}
.brand-name{font-size:13px;font-weight:600;line-height:13px;color:#333}
.brand-sub{font-size:8px;font-weight:600;color:#333;margin-top:6px;line-height:9px}
.search{position:absolute;left:817px;top:42px;width:172px;height:28px;border:1px solid #bfbfbf;border-radius:4px;background:linear-gradient(#fff,#e9e9e9)}
.search svg{position:absolute;right:-4px;top:6px}
.nav{position:absolute;left:280px;top:96px;display:flex;gap:5px}
.nav a{width:116px;height:37px;border-radius:4px;background:linear-gradient(var(--green-light),var(--green));color:#fff;font-size:14px;text-decoration:none;display:flex;align-items:center;justify-content:center;box-shadow:0 6px 6px -4px rgba(0,0,0,.1)}
.nav a.active{background:linear-gradient(#8a8a8a,#111 45%,#000)}
.hero{position:absolute;left:53px;top:153px;width:948px;height:349px;background:linear-gradient(#a9a398 0,#d8c3a4 45%,#b7a58e 70%,#5f6266 100%);box-shadow:0 14px 20px -8px rgba(0,0,0,.35)}
.dots{position:absolute;left:446px;top:483px;width:121px;height:40px;background:#ececec;border-radius:4px 4px 0 0;display:flex;gap:11px;justify-content:center;padding-top:11px}
.dots span{width:11px;height:11px;border-radius:50%;background:#c9c9c9}
.dots span.on{background:var(--green)}
.main{position:absolute;left:80px;top:544px;width:642px}
h1,h2{font-weight:400;color:var(--green)}
h1{font-size:24px;line-height:28px}
.lead{font-size:12px;line-height:24px;text-align:justify;margin:2px 0 0 3px}
.team-title{position:absolute;left:80px;top:705px;font-size:17px;line-height:24px;font-weight:600;color:var(--green)}
.team{position:absolute;left:80px;top:746px;width:642px;font-size:12px;line-height:18px}
.portal-title{position:absolute;left:80px;top:795px;font-size:18px;line-height:24px;font-weight:600;color:var(--green)}
.facts{position:absolute;left:90px;top:836px;list-style:none;font-size:12px;line-height:18px}
.divider{position:absolute;left:60px;top:878px;width:620px;height:8px;background:linear-gradient(90deg,rgba(230,242,211,0),var(--green-pale) 30%,var(--green-pale) 70%,rgba(230,242,211,0))}
.btn{position:absolute;left:635px;top:874px;width:97px;height:32px;border-radius:3px;background:linear-gradient(var(--green-light),var(--green));color:#fff;font-size:14px;display:flex;align-items:center;justify-content:center}
.aktuell-title{position:absolute;left:80px;top:896px;font-size:24px}
.gallery{position:absolute;left:54px;top:936px;width:678px;height:154px;background:linear-gradient(var(--green-dark),var(--green-light));border-radius:4px;display:flex;gap:4px;padding:17px 13px}
.gallery div{width:215px;height:120px}
.news{position:absolute;left:762px;top:556px;width:239px;height:452px;border:1px solid var(--green-light);border-radius:6px;background:linear-gradient(#fff 80%,#f3f9e9)}
.news h2{margin:8px 6px 0;height:48px;background:linear-gradient(var(--green-dark),var(--green-light));color:#fff;font-size:24px;padding:8px 0 0 37px}
.news-item{margin:15px 0 0 10px;width:215px}
.news-item .pic{height:120px}
.news-item p{height:46px;background:var(--green-pale);font-size:18px;padding:16px 0 0 46px;color:#333}
.news-more{position:absolute;right:16px;bottom:8px;font-size:14px;color:#555;display:flex;align-items:center;gap:6px}
.footer{position:absolute;left:0;top:1120px;width:1050px;height:80px;background:var(--green)}
.footer a{position:absolute;top:21px;color:#fff;font-size:14px;text-decoration:none}
.social{position:absolute;left:863px;top:19px;display:flex;gap:7px}
.social span{width:28px;height:28px;border-radius:50%;background:#fff;opacity:.85}
</style>
</head>
<body>
<header class="header">
  <div class="brand">
    <div class="brand-mark"></div>
    <div class="brand-name">PINECREST<br>&amp; TOURS</div>
    <div class="brand-sub">NORTHWAY HOTELS<br>&amp; PARTNERS</div>
  </div>
  <div class="search"><svg width="22" height="22" viewBox="0 0 22 22"><circle cx="9" cy="9" r="6" fill="none" stroke="#5b7fa8" stroke-width="2"/><line x1="13" y1="13" x2="20" y2="20" stroke="#444" stroke-width="3" stroke-linecap="round"/></svg></div>
  <nav class="nav">
    <a class="active" href="#">Home</a><a href="#">Hotel Finder</a><a href="#">Sofort-Wellness</a><a href="#">Specials</a><a href="#">e-Magazin</a><a href="#">Blog</a>
  </nav>
  <div class="hero" role="img" aria-label="Couple jumping joyfully on a beach at sunset"></div>
  <div class="dots"><span class="on"></span><span></span><span></span><span></span></div>
</header>

<main class="main">
  <h1>Welcome To Our Site</h1>
  <p class="lead">Lorem Ipsum is simply dummy text of the printing and typesetting industry. Lorem Ipsum has been the industry's standard dummy text ever since the 1500s, when an unknown printer took a galley of type and scrambled it to make a type specimen book. It has survived not only five centuries, but also the leap into electronic typesetting, remaining essentially unchanged. It was popularised in the 1960s with the release of Lettrix sheets containing Lorem Ipsum passages, and more recently with desktop publishing software like Quillset Layout including versions of Lorem Ipsum.</p>
</main>
<h3 class="team-title">DAS PINECREST-TEAM</h3>
<p class="team">präsentiert Ihnen unter dem Motto "Wellness auf einen Click" seit mehr als 11 Jahren Qualitätsgeprüfte Angebote rund um das Thema Wellness.</p>
<h4 class="portal-title">Auf unserem Wellness-Portal finden Sie</h4>
<ul class="facts">
  <li>Ca. 800 Wellness-Urlaube in außergewöhnlicher Wellness-Vielfalt - von klassisch über natürlich bis exotisch</li>
  <li>Ca. 150 Partner-Wellness-Hotels in sieben Europäischen Ländern</li>
</ul>
<div class="divider"></div>
<div class="btn">View More</div>
<h2 class="aktuell-title">Aktuelles</h2>
<section class="gallery">
  <div role="img" aria-label="Two women with towels and flowers at a spa" style="background:linear-gradient(#e9dcd0,#c98a78)"></div>
  <div role="img" aria-label="Man receiving a facial treatment" style="background:linear-gradient(#6b3a22,#c99a78)"></div>
  <div role="img" aria-label="Woman relaxing in a bath" style="background:linear-gradient(#3a2418,#d8b8a4)"></div>
</section>

<aside class="news">
  <h2>Latest News</h2>
  <div class="news-item"><div class="pic" role="img" aria-label="Woman under a pool waterfall" style="background:linear-gradient(#b9d9e2,#2f8fa8)"></div><p>LOREM IPSUM</p></div>
  <div class="news-item"><div class="pic" role="img" aria-label="Cup of tea with blossoms" style="background:linear-gradient(#c8b8a0,#9a5a2a)"></div><p>LOREM IPSUM</p></div>
  <div class="news-more">View More <svg width="13" height="13" viewBox="0 0 13 13"><circle cx="6.5" cy="6.5" r="6.5" fill="var(--green)"/><path d="M5 3.5l3 3-3 3" fill="none" stroke="#fff" stroke-width="1.6"/></svg></div>
</aside>

<footer class="footer">
  <a href="#" style="left:71px">Home</a><a href="#" style="left:179px">Hotel Finder</a><a href="#" style="left:293px">Sofort-Wellness</a><a href="#" style="left:432px">Specials</a><a href="#" style="left:551px">e-Magazin</a><a href="#" style="left:683px">Blog</a>
  <div class="social"><span></span><span></span><span></span><span></span></div>
</footer>
</body>
</html>
```